We want a business card/punch card for our business. We are including examples of our current business card (we like the front of our business card and not looking to remake it). We need only back side to be designed in form of a punch card (we are including a sample of the punch card we made, but are unsatisfied). For each $180 spend (9 punches) our clients have $20 off.

Colors
886aae

```html
<!DOCTYPE html>
<html lang="en">
<head>
<meta charset="utf-8">
<title>Lumina Methods – Customer Loyalty Card</title>
<link rel="stylesheet" href="https://fonts.googleapis.com/css2?family=Roboto+Condensed:wght@300;400;700&family=Parisienne&display=swap">
<style>
  :root {
    --card-bg: #b1bde3;
    --pattern-bg: #c3cdef;
    --band-purple: #5b2d8f;
    --band-lavender: #8e9bd3;
    --ink-purple: #5a3290;
    --brand-blue: #5a68bd;
    --punch-fill: #dde1ef;
    --dot: #d8ddf0;
  }
  html, body {
    margin: 0;
    padding: 0;
    width: 1200px;
    height: 686px;
    overflow: hidden;
    background: var(--card-bg);
  }
  .loyalty-card {
    position: relative;
    width: 1200px;
    height: 686px;
    overflow: hidden;
    background: var(--card-bg);
    font-family: "Roboto Condensed", "Arial Narrow", sans-serif;
    color: var(--ink-purple);
  }
  .card-shapes {
    position: absolute;
    inset: 0;
    width: 1200px;
    height: 686px;
  }
  .offer-line {
    position: absolute;
    left: 34px;
    top: 36px;
    margin: 0;
    font-weight: 400;
    font-size: 30px;
    line-height: 38px;
    white-space: nowrap;
  }
  .offer-line strong {
    font-weight: 700;
  }
  .punch-grid {
    position: absolute;
    left: 66px;
    top: 108px;
    display: grid;
    grid-template-columns: repeat(3, 122px);
    grid-template-rows: repeat(3, 122px);
    column-gap: 78px;
    row-gap: 15px;
    margin: 0;
    padding: 0;
    list-style: none;
  }
  .punch-slot {
    width: 122px;
    height: 122px;
    border-radius: 50%;
    background: var(--punch-fill);
  }
  .service-list {
    position: absolute;
    left: 36px;
    top: 572px;
    margin: 0;
    font-weight: 400;
    font-size: 27px;
    line-height: 46px;
    white-space: nowrap;
  }
  .service-list .sep {
    display: inline-block;
    width: 7px;
    height: 7px;
    margin: 0 5px;
    border-radius: 50%;
    background: var(--dot);
    vertical-align: middle;
  }
  .brand-name {
    position: absolute;
    left: 720px;
    width: 440px;
    top: 410px;
    margin: 0;
    text-align: center;
    font-weight: 400;
    font-size: 58px;
    line-height: 1;
    white-space: nowrap;
    color: var(--brand-blue);
  }
  .card-title {
    position: absolute;
    left: 666px;
    width: 534px;
    top: 568px;
    margin: 0;
    text-align: center;
    font-family: "Parisienne", cursive;
    font-weight: 400;
    font-size: 55px;
    line-height: 1;
    white-space: nowrap;
    color: var(--ink-purple);
  }
</style>
</head>
<body>
<main class="loyalty-card">
  <svg class="card-shapes" viewBox="0 0 1200 686">
    <path class="lavender-band" fill="var(--band-lavender)"
          d="M748 0 L808 0 C775 80 735 160 695 250 C705 170 728 90 748 0 Z"/>
    <path class="purple-band" fill="var(--band-purple)"
          d="M792 0 C752 140 678 230 652 400 C636 520 630 610 632 686 L1200 686 L1200 0 Z"/>
    <path class="pattern-panel" fill="var(--pattern-bg)" role="img"
          aria-label="Soft lavender mandala pattern backdrop"
          d="M842 0 C796 140 722 235 696 400 C680 520 676 610 678 686 L1200 686 L1200 0 Z"/>
  </svg>

  <p class="offer-line">For every $180 spent, you’ll recieve <strong>$20 off your next visit!</strong></p>

  <ul class="punch-grid" aria-label="Nine punch slots">
    <li class="punch-slot"></li>
    <li class="punch-slot"></li>
    <li class="punch-slot"></li>
    <li class="punch-slot"></li>
    <li class="punch-slot"></li>
    <li class="punch-slot"></li>
    <li class="punch-slot"></li>
    <li class="punch-slot"></li>
    <li class="punch-slot"></li>
  </ul>

  <p class="service-list">
    Tantra<span class="sep"></span>Sexual Healing<span class="sep"></span>Intomacy Coaching<br>
    Sound Healing<span class="sep"></span>Sound Baths<span class="sep"></span>Crystal Healing<span class="sep"></span>Yoga
  </p>

  <h1 class="brand-name">Lumina Methods</h1>
  <h2 class="card-title">Customer Loyalty Card</h2>
</main>
</body>
</html>
```